Stationary package for modern new church start
Stationary for Bright Harbor Ministries
Stationary package for modern new church start  - Religion and Spirituality
Creative Brief
Professional
Daniel Mercer
Pastor
Bright Harbor Ministries P.O. Box 67890 Atlanta, GA 30318 The following P.O. Box is a generate one until I obtain one tomorrow. I will provide you with the correct P.O. Box sometime tomorrow or on Friday.
pastormercer@bhmx.org
www.bhmx.org
Please provide me with a complete stationary package that includes: Business Cards Letterhead Pen and pencil Email Signature USB Envelope Folder Fax Option Thank you Card front & Back Compliment Slip CD and CD Cover
Please include the following on the back: The Logo our our Ministry and our email address

```html
<!DOCTYPE html>
<html lang="en">
<head>
<meta charset="utf-8">
<title>Bright Harbor Ministries – Business Card</title>
<link rel="stylesheet" href="https://fonts.googleapis.com/css2?family=Exo+2:wght@400;600;700&display=swap">
<style>
  :root {
    --red: #e0202a;
    --red-dark: #b3121b;
    --blue: #2d8fd0;
    --ink: #3a3a3a;
    --muted: #6b6b6b;
    --paper: #ffffff;
    --stage: #e6e7e9;
  }
  * { box-sizing: border-box; margin: 0; padding: 0; }
  html, body { width: 1200px; height: 898px; overflow: hidden; }
  body {
    background: var(--stage);
    font-family: "Exo 2", Arial, sans-serif;
    color: var(--ink);
    display: flex; align-items: center; justify-content: center; gap: 48px;
  }
  .card {
    position: relative;
    width: 520px; height: 300px;
    background: var(--paper);
    border-radius: 22px;
    overflow: hidden;
    box-shadow: 0 4px 14px rgba(0,0,0,.12);
  }
  .brand { display: flex; align-items: center; gap: 8px; }
  .brand-dot { width: 30px; height: 30px; border-radius: 50%; background: var(--red); flex: none; }
  .brand-name { font-weight: 700; color: var(--red); font-size: 17px; line-height: 1.05; }
  .brand-tagline { font-size: 7px; color: var(--muted); letter-spacing: .5px; margin-top: 2px; }

  .front .brand { position: absolute; left: 26px; top: 22px; }
  .front .brand-name { width: 120px; }
  .address { position: absolute; left: 28px; top: 90px; font-size: 10px; line-height: 1.4; color: var(--ink); }
  .contacts { position: absolute; left: 28px; top: 128px; list-style: none; font-size: 9px; color: var(--muted); }
  .contacts li { display: flex; align-items: center; gap: 7px; height: 16px; }
  .contacts svg { width: 10px; height: 10px; fill: var(--red); }
  .person { position: absolute; right: 40px; top: 78px; text-align: right; }
  .person-name { color: var(--red); font-size: 19px; font-weight: 600; letter-spacing: 1px; text-transform: uppercase; }
  .person-role { font-size: 13px; letter-spacing: .8px; text-transform: uppercase; margin-top: 4px; }
  .front .brand.stacked { left: auto; right: 76px; top: 136px; flex-direction: column; gap: 6px; text-align: center; }
  .front .brand.stacked .brand-dot { width: 44px; height: 44px; }
  .band { position: absolute; left: 0; bottom: 0; width: 520px; height: 90px; }
  .band-url { position: absolute; right: 34px; bottom: 18px; color: #fff; font-size: 11px; letter-spacing: .5px; }

  .back { background: linear-gradient(180deg, #ffffff 0%, #eeeeee 100%); }
  .back .brand { position: absolute; inset: 0; justify-content: center; gap: 14px; }
  .back .brand-dot { width: 64px; height: 64px; }
  .back .brand-name { font-size: 30px; width: 240px; }
  .back .brand-tagline { font-size: 10px; }
</style>
</head>
<body>
  <section class="card front">
    <div class="brand">
      <span class="brand-dot"></span>
      <div>
        <div class="brand-name">Bright Harbor Ministries</div>
        <div class="brand-tagline">Sharing His Love Daily</div>
      </div>
    </div>

    <p class="address">214 Harbor Lane, Suite 9<br>Atlanta</p>

    <ul class="contacts">
      <li><svg viewBox="0 0 10 10"><path d="M2 0h2l1 3-1.5 1a6 6 0 0 0 2.5 2.5L7 5l3 1v2c0 1-1 2-2 2A8 8 0 0 1 0 2c0-1 1-2 2-2z"/></svg>012 555 0147</li>
      <li><svg viewBox="0 0 10 10"><path d="M2 0h2l1 3-1.5 1a6 6 0 0 0 2.5 2.5L7 5l3 1v2c0 1-1 2-2 2A8 8 0 0 1 0 2c0-1 1-2 2-2z"/></svg>012 555 0148</li>
      <li><svg viewBox="0 0 10 10"><rect x="2" y="0" width="6" height="3"/><rect x="0" y="3" width="10" height="5" rx="1"/><rect x="2" y="7" width="6" height="3"/></svg>012 555 0149</li>
      <li><svg viewBox="0 0 10 10"><rect x="0" y="1.5" width="10" height="7" rx="1"/><path d="M0 2l5 4 5-4" stroke="#fff" fill="none"/></svg>pastormercer@bhmx.org</li>
      <li><svg viewBox="0 0 10 10"><circle cx="5" cy="5" r="5"/><path d="M0 5h10M5 0v10" stroke="#fff" stroke-width=".8"/></svg>www.bhmx.org</li>
    </ul>

    <div class="person">
      <div class="person-name">Marcus Whitfield</div>
      <div class="person-role">Financial Advisor</div>
    </div>

    <div class="brand stacked">
      <span class="brand-dot"></span>
      <div>
        <div class="brand-name">Bright Harbor<br>Ministries</div>
        <div class="brand-tagline">Sharing His Love Daily</div>
      </div>
    </div>

    <svg class="band" viewBox="0 0 520 90" preserveAspectRatio="none" aria-hidden="true">
      <path d="M0 22 C140 48 330 52 520 30 L520 36 C330 58 140 54 0 30 Z" fill="var(--blue)"/>
      <path d="M0 34 C140 60 330 62 520 40 L520 90 L0 90 Z" fill="var(--red)"/>
      <path d="M0 70 C160 80 340 74 520 60 L520 90 L0 90 Z" fill="var(--red-dark)" opacity=".45"/>
    </svg>
    <div class="band-url">www.bhmx.org</div>
  </section>

  <section class="card back">
    <div class="brand">
      <span class="brand-dot"></span>
      <div>
        <div class="brand-name">Bright Harbor Ministries</div>
        <div class="brand-tagline">Sharing His Love Daily</div>
      </div>
    </div>
  </section>
</body>
</html>
```